Wine Label Design-Crumbled Ledge Vineyard

Crumbled Ledge Vineyard is in the Barossa Valley in South Australia. The Barossa is recognized as Australia's premier wine region, producing Australia's icon wines and some " new takes on traditional".
This family owned and operated vineyard grows some exceptionally high quality fruit. Most of the fruit is sold and used for some of Australia's most iconic wines. Small quantities are retained by the owners for some wines with very limited availability. (Wines were previously sold as BrellMarston Vineyards Crumbled Ledge ( Shiraz, Cabernet etc).

The wines will in the future be labeled simply ‘Crumbled Ledge Vineyard’. The label will launch this new identity for the single family single vineyard and its high quality wines which are a true expression of the vineyard and derive from the Crumbled Ledge common to this ancient area (800-2000 million years old).
The label should reflect
• Single vineyard, family owned
• vines in very old rock & soils
• High quality & reliability
• Edgy but true, design based thinking (Please note:blue is generally seen as an unacceptable colour for a wine label?? Don’t ask me why)

The wines will be sold mostly direct in Australia ( ie not through retail stores), with limited export to Asia, Scandinavia and Canada.
There are three quality levels and price points in the portfolio
1. Entry level premium for everyday drinking for discriminating drinkers-approx AUD20
2. Super Premium-approx AUD30
3. Limited Release ultlra premium-AUD75-90?
We envisage three variations on the label but with an obvious & common design element. This design element should be able to be used for corporate identification and promotion
The paper stock will be waterproof and self adhesive. Our preference is for designs that engage the user by appealing to both sight and touch. It is preferred that textures be added eg embossing, high build varnish etc-rather than be a facet of the stock itself.
For information on statutory label requirements refer to www.vinoregistry-example.com . In brief
o Front label need not show any mandatory information. However we would prefer Variety, Barossa Valley, Year and alcohol to be shown on the front label
o Back label should show all mandatories and allow for a bar code

Reason: I've had a problem with my wireless broadband account and reception has been intermittent to say the least to the extent that I switched off at the weekend. Just going downtown now for a 'polite discussion' with my service provider.

Reason: I have receiver insufficient designs of quality which we would consider. Too many designs have a "cut and paste" appearance - too few exhibit an original art/design element which truly identifies the product.

Gals & Guys

most of the designs submitted lack punch and originality and are totally unmemorable.
Please-get on Zindle or whatever enter "Wine Label Designs" and do some research b4 u waste your time and mine. Formulaic cut and paste will not win the day. That's not to say that cut and paste can't work-but it must have some originality, impact and command attention. Please surprise me.

Following on from a question from a designer about who is our competition and what we are looking for I sent the following 
"I don't think I can add anything new. Read the brief and comments again and research wine labels on the web. In 30 minutes you'll get a good idea of the creative edgy designs in the industry. There are a plethora of collections. Our competition-anyone with a label. In 2010 there were over 2400 "producers" in other words 2400 producers with at least one label. In fact there are over 25000 Australian wines and then the numerous imported wines.

Target Market(s)

$20 people who budget everyday but have graduated from drinking 'entry level' wines. These people will likely fit into Cat. (b) in the $30 wine

$30 (a) will not over-compromise on some everyday discretionary expenditure.(b) might buy for special occasions

$70-$90 Professional/successful people with high disposable/discretionary income not particularly worried about recession. wine geeks.

Industry/Entity Type

Retail

Requirements
Must have
• identifiable element across range of wines

```html
<!DOCTYPE html>
<html lang="en">
<head>
<meta charset="utf-8">
<title>Crumbled Ledge Vineyards – Wine Labels</title>
<link rel="stylesheet" href="https://fonts.googleapis.com/css2?family=Open+Sans:wght@700;800&display=swap">
<style>
  :root {
    --gold: #c0852e;
    --frame: #b97f2c;
    --ink: #000000;
    --paper: #ffffff;
    --rock-light: #6a6e72;
    --rock-mid: #2c2e31;
    --purple: #6b2f8c;
    --grape: #6a2a5c;
  }
  * { margin: 0; padding: 0; box-sizing: border-box; }
  html, body {
    width: 1200px; height: 797px; overflow: hidden;
    background: var(--paper);
    font-family: "Open Sans", Arial, sans-serif;
  }
  .stage {
    position: relative; width: 1300px; height: 863px;
    transform: scale(0.92308); transform-origin: 0 0;
  }
  .label {
    position: absolute; top: 75px; width: 473px; height: 710px;
    background: var(--frame);
  }
  .label--front { left: 75px; }
  .label--back { left: 748px; }
  .label__face {
    position: absolute; left: 17px; top: 22px; right: 18px; bottom: 30px;
    background: var(--ink); overflow: hidden;
  }
  .rock-field {
    position: absolute; border-radius: 50%;
    background: radial-gradient(circle, var(--rock-light) 0%, var(--rock-mid) 45%, var(--ink) 72%);
  }
  .label--front .rock-field { left: -10px; top: 110px; width: 460px; height: 460px; }
  .label--back .rock-field { left: 0; top: 80px; width: 440px; height: 440px; }

  .vine-art {
    position: absolute; left: 43px; top: 222px; width: 345px; height: 228px;
    border-radius: 46% 40% 44% 50%;
    background:
      radial-gradient(ellipse 30% 42% at 82% 62%, var(--grape) 0%, var(--grape) 60%, rgba(106,42,92,0) 100%),
      radial-gradient(ellipse 60% 55% at 42% 45%, rgba(192,133,46,0.85) 0%, rgba(192,133,46,0.55) 50%, rgba(107,47,140,0.45) 80%, rgba(107,47,140,0) 100%);
  }

  .gold { color: var(--gold); }
  .rule { position: absolute; height: 7px; background: var(--gold); }
  .centered { position: absolute; left: 0; right: 0; text-align: center; font-weight: 700; color: var(--gold); }

  .brand__mark {
    position: absolute; left: 40px; top: 20px; width: 50px; height: 50px;
    border-radius: 50%; background: var(--purple);
  }
  .brand__name { position: absolute; left: 108px; top: 40px; font-size: 23px; font-weight: 700; color: var(--gold); letter-spacing: 0.5px; }
  .brand__sub { top: 76px; font-size: 23px; }
  .front__region { top: 514px; font-size: 27px; }
  .front__year { top: 558px; font-size: 33px; }
  .front__variety { top: 606px; font-size: 27px; }

  .back__heading { top: 22px; font-size: 18px; }
  .back__story {
    position: absolute; left: 0; right: 0; top: 74px;
    text-align: center; color: var(--paper); font-size: 14px; font-weight: 700; line-height: 20px;
  }
  .back__drinks { top: 446px; font-size: 18px; }
  .back__facts {
    position: absolute; left: 13px; top: 476px;
    color: var(--paper); font-size: 14px; font-weight: 700; line-height: 20px;
  }
  .barcode-space { position: absolute; left: 282px; top: 525px; width: 138px; height: 108px; background: var(--paper); }
</style>
</head>
<body>
<main class="stage">

  <section class="label label--front" aria-label="Front label">
    <div class="label__face">
      <div class="rock-field" role="img" aria-label="Mosaic of shattered rock pieces glowing from the centre"></div>
      <div class="vine-art" role="img" aria-label="Golden curling grapevine with purple leaves and a deep purple grape bunch"></div>

      <span class="brand__mark" aria-hidden="true"></span>
      <p class="brand__name">CRUMBLED LEDGE</p>
      <div class="rule" style="left:0; top:88px; width:113px;"></div>
      <p class="centered brand__sub">VINEYARDS</p>
      <div class="rule" style="left:327px; top:88px; width:113px;"></div>

      <p class="centered front__region">Barossa Valley</p>
      <div class="rule" style="left:21px; top:577px; width:135px;"></div>
      <p class="centered front__year">2012</p>
      <div class="rule" style="left:280px; top:577px; width:135px;"></div>
      <p class="centered front__variety">Bordeaux</p>
    </div>
  </section>

  <section class="label label--back" aria-label="Back label">
    <div class="label__face">
      <div class="rock-field" role="img" aria-label="Mosaic of shattered rock pieces glowing from the centre"></div>

      <p class="centered back__heading">Bordeaux * 2012 * Barossa Valley</p>
      <p class="back__story">
        <span class="gold">O</span>ur wines are planted on areas which<br>
        are characterized by enormous<br>
        quantities of shattered shale, slate, and<br>
        limestone based rock.<br>
        <span class="gold">T</span>he shattered shale and limestone<br>
        based rocks &nbsp;give name to our premium<br>
        line. They are present throughout the<br>
        vineyards and are a major component<br>
        of the unique nature of the differing<br>
        terroirs and contribute to the wines<br>
        with tight structure and minerality yet<br>
        abundant and generous fruit.<br>
        <span class="gold">O</span>ur wines drink well from release. Reds<br>
        from 2 to 3 years from vintage.<br>
        Cellaring potential varies between<br>
        vintages but as a general rule they<br>
        drink best in the range of 6 to 12 years<br>
        of age
      </p>
      <p class="centered back__drinks">Contains approx. 8.3 Standard Drinks</p>
      <div class="back__facts">
        750mL<br>
        Wine Of &nbsp;Australia<br>
        13.5% ALC/VOL<br>
        CONTAINS SULFATES<br>
        PRODUCED WITH MILK PRODUCTS<br>
        <span class="gold">Crumbled Ledge Vineyards</span><br>
        Lot 7 Ferrow Lane, Kelbury, SA<br>
        5999 Australia
      </div>
      <div class="barcode-space" aria-label="Space reserved for barcode"></div>
    </div>
  </section>

</main>
</body>
</html>
```